I need to redesign this website. Modern Fun Professional Redesign For www.GladPerksHub.com = New Name www.ClaimVouchly.com

Use existing content as it is on website exactly and we will revise after initial mock ups.

The new name will be ClaimVouchly.com please make a quick logo for this site too while redesigning.

Make it look like an official website....

Target Market(s)

Consumers that are redeeming certificates that businesses gave to them as a gift for customer loyalty,e tc.

Industry/Entity Type

It Professional

Logo Text

www.ClaimVouchly.com

Number of Pages Required

4 page

Colors

Designer to choose colors to be used in the design.

Requirements
Must have
• Must look professional, build trust and credibility.
Nice to have
• open
Should not have
• open

```html
<!DOCTYPE html>
<html lang="en">
<head>
<meta charset="utf-8">
<title>ClaimVouchly – Redeem Processing Center</title>
<link href="https://fonts.googleapis.com/css2?family=Montserrat:wght@600;700;800&family=Mulish:ital,wght@0,400;0,600;0,700;1,400&display=swap" rel="stylesheet">
<style>
:root{
  --orange:#f07427;
  --orange-dark:#e0621a;
  --teal:#4db7c8;
  --gold:#c98b22;
  --gold-light:#d9a03a;
  --dark:#333333;
  --ink:#555555;
  --white:#ffffff;
  --field:#f4f4f4;
}
*{box-sizing:border-box;margin:0;padding:0}
html,body{width:1200px;height:3249px;overflow:hidden;background:var(--white)}
body{position:relative;font-family:"Mulish",sans-serif;color:var(--ink)}
.abs{position:absolute}
.heading{font-family:"Montserrat",sans-serif;font-weight:800;text-transform:uppercase;letter-spacing:.5px}
.btn{position:absolute;display:flex;align-items:center;justify-content:center;gap:14px;border-radius:40px;
  background:linear-gradient(var(--gold-light),var(--gold));color:var(--white);font-family:"Montserrat",sans-serif;
  font-weight:700;text-transform:uppercase;letter-spacing:1px;box-shadow:0 4px 6px rgba(0,0,0,.25)}
.btn .arrow{width:24px;height:24px;border:2px solid var(--white);border-radius:50%;display:flex;align-items:center;justify-content:center}

/* header */
.site-header{position:absolute;left:0;top:0;width:1200px;height:115px;background:var(--white)}
.brand{position:absolute;left:75px;top:28px;display:flex;align-items:center;gap:10px}
.brand-dot{width:22px;height:22px;border-radius:50%;background:var(--gold-light)}
.brand-name{font-family:"Montserrat",sans-serif;font-weight:700;font-size:28px;color:var(--orange)}
.brand-tag{position:absolute;left:107px;top:68px;font-size:12px;font-weight:700;color:var(--dark)}
.main-nav{position:absolute;top:36px;left:596px;display:flex;align-items:center;font-size:16px;color:var(--ink);font-family:"Mulish",sans-serif}
.main-nav a{text-decoration:none;color:inherit;margin-right:38px}
.main-nav .active{background:var(--gold);color:var(--white);padding:12px 26px;border-radius:30px;margin-right:34px}

/* hero */
.hero{position:absolute;left:0;top:115px;width:1200px;height:590px;overflow:hidden}
.hero-photo{position:absolute;inset:0;background:radial-gradient(circle at 18% 30%,#3a7fb0 0,#1b2a4a 22%,transparent 40%),linear-gradient(120deg,#1a1410 0%,#4a3218 45%,#6a4a24 60%,#20160e 100%)}
.hero-title{position:absolute;right:80px;top:120px;text-align:right;font-family:"Montserrat",sans-serif;font-weight:700;font-size:43px;line-height:57px;color:var(--white)}
.hero-arrow{position:absolute;top:205px}

/* welcome */
.welcome{position:absolute;left:0;top:680px;width:1200px;height:332px;background:var(--orange)}
.welcome .heading{position:absolute;top:58px;width:100%;text-align:center;font-size:40px;color:var(--white)}
.welcome p{position:absolute;top:128px;left:220px;width:760px;text-align:center;color:var(--white);font-style:italic;font-size:17px;line-height:29px}
.cert-form{position:absolute;left:340px;top:210px;width:520px;height:60px;background:var(--white);border-radius:30px}
.cert-form span{position:absolute;left:28px;top:20px;font-size:14px;font-style:italic;color:#888}
.cert-form .go{position:absolute;right:6px;top:6px;width:48px;height:48px;border-radius:50%;background:var(--gold);color:var(--white);font-family:"Montserrat",sans-serif;font-weight:700;font-size:16px;display:flex;align-items:center;justify-content:center}

/* about */
.about .heading{position:absolute;top:1070px;width:100%;text-align:center;font-size:40px;color:var(--orange)}
.about-illustration{position:absolute;left:450px;top:1180px;width:296px;height:232px;border-radius:14px;background:linear-gradient(180deg,#7cc9e8 0%,#d9e9f0 45%,#e0a048 70%,#c47a22 100%)}
.about-col{position:absolute;top:1435px;width:478px;font-size:13.5px;line-height:27.5px;color:var(--ink)}
.about-col.left{left:115px;text-align:right}
.about-col.right{left:608px}

/* contact */
.contact .heading{position:absolute;left:0;width:600px;top:1808px;text-align:center;font-size:38px;color:var(--white)}
.contact-intro{position:absolute;left:70px;width:460px;top:1880px;text-align:center;color:var(--white);font-size:15.5px;line-height:27px}
.field{position:absolute;background:var(--field);font-size:13px;color:#777;padding:14px 14px}
.video-photo{position:absolute;left:600px;top:1710px;width:600px;height:655px}

/* testimonials */
.testimonials .heading{position:absolute;top:2430px;width:100%;text-align:center;font-size:40px;color:var(--orange)}
.avatar{position:absolute;left:512px;top:2508px;width:178px;height:178px;border-radius:50%;border:10px solid var(--white);box-shadow:0 0 10px rgba(0,0,0,.2);background:linear-gradient(160deg,#6a90b8,#3a4e68)}
.quote{position:absolute;left:120px;top:2712px;width:960px;text-align:center;font-size:15px;line-height:31px;color:var(--ink)}
.quote b{color:var(--orange);font-size:26px;font-family:"Montserrat",sans-serif}
.author{position:absolute;top:2788px;width:100%;text-align:center;font-size:15px}
.author strong{color:var(--gold);font-family:"Montserrat",sans-serif}

/* footer */
.site-footer{position:absolute;left:0;top:2905px;width:1200px;height:290px;background:var(--dark);color:#bbb}
.foot-title{position:absolute;top:53px;font-family:"Montserrat",sans-serif;font-weight:700;font-size:16px;color:var(--orange);letter-spacing:.5px}
.foot-list{position:absolute;top:95px;list-style:none;font-size:14px;line-height:29px}
.foot-list li::before{content:"";display:inline-block;width:9px;height:9px;border-radius:50%;background:var(--orange);margin-right:12px}
.foot-text{position:absolute;font-size:14px;line-height:27px}
.email-box{position:absolute;left:607px;top:165px;width:250px;height:42px;background:var(--white);font-size:13px;color:#666;padding:12px 10px}
.social{position:absolute;top:170px;width:44px;height:44px;border-radius:50%;border:2px solid var(--gold-light);background:var(--gold)}
.copyright{position:absolute;left:0;top:3190px;width:1200px;height:59px;background:var(--orange);color:var(--white);text-align:center;font-size:14px;line-height:59px}
</style>
</head>
<body>

<header class="site-header">
  <div class="brand"><span class="brand-dot"></span><span class="brand-name">ClaimVouchly</span></div>
  <div class="brand-tag">Redeem Processing Center</div>
  <nav class="main-nav">
    <a class="active">HOME</a><a>CONTACT US</a><a>TESTIMONIALS</a><a>TERMS</a>
    <svg width="22" height="22" viewBox="0 0 22 22"><circle cx="9" cy="9" r="7" fill="none" stroke="#f07427" stroke-width="3"/><line x1="14" y1="14" x2="20" y2="20" stroke="#f07427" stroke-width="3"/></svg>
  </nav>
</header>

<section class="hero">
  <div class="hero-photo" role="img" aria-label="Night photo of a neon hot-air balloon sign in front of a lit city hotel"></div>
  <svg class="hero-arrow" style="left:14px" width="30" height="60" viewBox="0 0 30 60"><polyline points="26,2 4,30 26,58" fill="none" stroke="#fff" stroke-width="2"/></svg>
  <svg class="hero-arrow" style="right:14px" width="30" height="60" viewBox="0 0 30 60"><polyline points="4,2 26,30 4,58" fill="none" stroke="#fff" stroke-width="2"/></svg>
  <h1 class="hero-title">What Good Is It To Receive<br>A Gift Certificate If You<br>Can't Use It?</h1>
  <div class="btn" style="left:876px;top:310px;width:246px;height:62px;font-size:21px">Contact Us <span class="arrow"><svg width="12" height="12" viewBox="0 0 12 12"><path d="M1 6h9M6 2l4 4-4 4" fill="none" stroke="#fff" stroke-width="2"/></svg></span></div>
  <svg class="abs" style="left:0;bottom:0" width="1200" height="80" viewBox="0 0 1200 80"><path d="M0 80 L0 40 Q300 -10 620 40 T1200 20 L1200 80 Z" fill="#fff"/><path d="M0 80 L0 56 Q300 10 620 56 T1200 40 L1200 80 Z" fill="#f07427"/></svg>
</section>

<section class="welcome">
  <h2 class="heading">Welcome to <span style="color:var(--teal)">ClaimVouchly</span></h2>
  <svg class="abs" style="left:600px;top:100px" width="290" height="20" viewBox="0 0 290 20"><path d="M2 16 Q140 0 288 10" fill="none" stroke="#fff" stroke-width="3"/></svg>
  <p>Please Enter a Valid Certificate Id In The Form Below To redeem Your Certificate And To View Faq's,Terms and Locations.</p>
  <div class="cert-form"><span>Certificate Id *</span><div class="go">GO</div></div>
</section>

<section class="about">
  <h2 class="heading">About <span style="color:var(--teal)">ClaimVouchly</span></h2>
  <svg class="abs" style="left:540px;top:1112px" width="280" height="20" viewBox="0 0 280 20"><path d="M2 16 Q140 0 278 10" fill="none" stroke="#f07427" stroke-width="3"/></svg>
  <div class="about-illustration" role="img" aria-label="Illustration of an open suitcase filled with travel landmarks"></div>
  <p class="about-col left">Lorem Ipsum is simply dummy text of the printing and typesetting industry. Lorem Ipsum has been the industry's standard dummy text ever since the 1500s, when an unknown printer took a galley of type and scrambled it to make a type specimen book. It has survived not only five centuries, but also the leap into electronic typesetting,</p>
  <p class="about-col right">Lorem Ipsum is simply dummy text of the printing and typesetting industry. Lorem Ipsum has been the industry's standard dummy text ever since the 1500s, when an unknown printer took a galley of type and scrambled it to make a type specimen book. It has survived not only five centuries, but also the leap into electronic typesetting,</p>
  <div class="btn" style="left:472px;top:1590px;width:250px;height:60px;font-size:21px">Know More <span class="arrow"><svg width="12" height="12" viewBox="0 0 12 12"><path d="M1 6h9M6 2l4 4-4 4" fill="none" stroke="#fff" stroke-width="2"/></svg></span></div>
</section>

<section class="contact">
  <svg class="abs" style="left:0;top:1700px" width="1200" height="670" viewBox="0 0 1200 670">
    <path d="M0 10 Q300 40 600 0 L600 670 L0 650 Z" fill="#f07427"/>
  </svg>
  <div class="video-photo" role="img" aria-label="Photo of a smiling couple looking at a travel brochure" style="background:linear-gradient(135deg,#2f4d3a 0%,#6d8a78 35%,#c9a38e 60%,#e8d8cc 100%)"></div>
  <svg class="abs" style="left:0;top:2330px" width="1200" height="45" viewBox="0 0 1200 45"><path d="M0 30 Q300 0 600 20 Q900 40 1200 10 L1200 45 L0 45 Z" fill="#fff"/></svg>
  <svg class="abs" style="left:850px;top:1980px" width="112" height="112" viewBox="0 0 112 112"><circle cx="56" cy="56" r="52" fill="#fff" stroke="#d62828" stroke-width="4"/><circle cx="56" cy="56" r="44" fill="#e02a2a"/><path d="M44 34 L76 56 L44 78 Z" fill="#fff"/></svg>
  <h2 class="heading">Contact <span style="color:var(--teal)">Form</span></h2>
  <svg class="abs" style="left:330px;top:1848px" width="130" height="16" viewBox="0 0 130 16"><path d="M2 13 Q65 0 128 8" fill="none" stroke="#fff" stroke-width="3"/></svg>
  <p class="contact-intro">If you have any questions about how to redeem a certain certificate, please contact us. We are here to help.</p>
  <div class="field" style="left:83px;top:1945px;width:434px;height:48px">Name*</div>
  <div class="field" style="left:83px;top:2000px;width:214px;height:48px">Eamil*</div>
  <div class="field" style="left:302px;top:2000px;width:215px;height:48px">Phone*</div>
  <div class="field" style="left:83px;top:2055px;width:434px;height:48px">Certificate ID #*</div>
  <div class="field" style="left:83px;top:2110px;width:434px;height:90px">How May We Assist You?*</div>
  <div class="btn" style="left:200px;top:2205px;width:190px;height:60px;font-size:21px">Submit <span class="arrow"><svg width="12" height="12" viewBox="0 0 12 12"><path d="M1 6h9M6 2l4 4-4 4" fill="none" stroke="#fff" stroke-width="2"/></svg></span></div>
</section>

<section class="testimonials">
  <h2 class="heading">Waht Oue Client <span style="color:var(--teal)">Say About Us</span></h2>
  <svg class="abs" style="left:720px;top:2470px" width="220" height="18" viewBox="0 0 220 18"><path d="M2 14 Q110 0 218 8" fill="none" stroke="#f07427" stroke-width="3"/></svg>
  <svg class="abs" style="left:422px;top:2580px" width="18" height="40" viewBox="0 0 18 40"><polyline points="16,2 2,20 16,38" fill="none" stroke="#aaa" stroke-width="2"/></svg>
  <svg class="abs" style="left:760px;top:2580px" width="18" height="40" viewBox="0 0 18 40"><polyline points="2,2 16,20 2,38" fill="none" stroke="#aaa" stroke-width="2"/></svg>
  <div class="avatar" role="img" aria-label="Client photo of a couple"></div>
  <p class="quote"><b>“</b> I am extremely happy with my service, everything worked out perfect. My wife and I had a great time in Las Vegas. The hotel we stayed at was very nice and clean. I would go there again. Thank you for everything. <b>”</b></p>
  <p class="author"><span style="display:inline-block;width:20px;height:3px;background:var(--gold);vertical-align:middle;margin-right:10px"></span><strong>Mark T.</strong> ( Ridgeview, CA )</p>
</section>

<svg class="abs" style="left:0;top:2880px" width="1200" height="40" viewBox="0 0 1200 40"><path d="M0 40 L0 30 Q600 -10 1200 10 L1200 40 Z" fill="#f07427"/><path d="M0 40 L0 38 Q600 2 1200 20 L1200 40 Z" fill="#333"/></svg>

<footer class="site-footer">
  <h3 class="foot-title" style="left:78px">SITE MAP</h3>
  <ul class="foot-list" style="left:78px"><li>Home</li><li>Contact Us</li><li>Testimonials</li><li>Terms</li></ul>
  <h3 class="foot-title" style="left:345px">MAILING ADDRESS</h3>
  <svg class="abs" style="left:342px;top:98px" width="22" height="16" viewBox="0 0 22 16"><rect width="22" height="16" rx="2" fill="#f07427"/><path d="M1 2 L11 9 L21 2" fill="none" stroke="#333" stroke-width="2"/></svg>
  <p class="foot-text" style="left:376px;top:88px">Mail Us On :<br>The Claim Center<br>4210 Marlow Ave Ste B #118<br>Fair Oaks, Ca 95628</p>
  <h3 class="foot-title" style="left:607px">NEWSLETTER</h3>
  <p class="foot-text" style="left:607px;top:88px;width:260px;line-height:25px">Would you like to receive exclusive access to articles, white papers and our regular monthly newsletter?</p>
  <div class="email-box">Enter Email*</div>
  <div class="btn" style="left:607px;top:218px;width:180px;height:42px;font-size:15px">Subscribe <span class="arrow" style="width:20px;height:20px"><svg width="10" height="10" viewBox="0 0 12 12"><path d="M1 6h9M6 2l4 4-4 4" fill="none" stroke="#fff" stroke-width="2"/></svg></span></div>
  <div class="abs" style="left:880px;top:88px;display:flex;align-items:center;gap:8px"><span class="brand-dot"></span><span class="brand-name" style="font-size:28px">ClaimVouchly</span></div>
  <p class="abs" style="left:915px;top:132px;font-size:13px;color:#fff">Redeem Processing Center</p>
  <span class="social" style="left:916px"></span><span class="social" style="left:970px"></span><span class="social" style="left:1024px"></span>
</footer>
<div class="copyright">©ClaimVouchly - 2017 All Rights Reserved</div>

</body>
</html>
```